New business card for civil engineering company - "Keystone Audit"

We need a business card designed for our new structural engineering company.

The company name is "Keystone Audit" logo files attached.

We would like the following:
* Two-sided card
* Simple design

Information to be placed on the card:
Name - Marcus Dellow
Job Title - Director / Structural Engineer
Credentials - BEng(Hons), CPEng, CMengNZ, IntPE(NZ)
Email - marcus.dellow@keystoneaudit.co.nz
mobile - 0219364058
website - www.keystoneaudit.co.nz

```html
<!DOCTYPE html>
<html lang="en">
<head>
<meta charset="utf-8">
<title>Keystone Audit – Business Card</title>
<link rel="stylesheet" href="https://fonts.googleapis.com/css2?family=Barlow:wght@400;500;700&display=swap">
<style>
  :root {
    --page-bg: #ffffff;
    --frame-navy: #07446f;
    --shadow-navy: #000a2e;
    --card-white: #ffffff;
    --accent-blue: #1e73be;
    --text-grey: #3a3a3a;
  }
  * { margin: 0; padding: 0; box-sizing: border-box; }
  html, body {
    width: 1200px;
    height: 1000px;
    overflow: hidden;
    background: var(--page-bg);
  }
  .canvas {
    position: relative;
    width: 1200px;
    height: 1000px;
    font-family: "Barlow", "Helvetica Neue", Arial, sans-serif;
  }
  .card-back {
    position: absolute;
    left: 69px;
    top: 206px;
    width: 1062px;
    height: 589px;
    background: var(--frame-navy);
  }
  .card-shadow {
    position: absolute;
    left: 129px;
    top: 730px;
    width: 943px;
    height: 26px;
  }
  .card-front {
    position: absolute;
    left: 129px;
    top: 262px;
    width: 943px;
    height: 474px;
    background: var(--card-white);
    text-align: center;
  }
  .person-name {
    position: absolute;
    left: 0; right: 0;
    top: 82px;
    font-size: 44px;
    font-weight: 700;
    letter-spacing: 1px;
    color: var(--accent-blue);
    line-height: 1;
  }
  .job-title {
    position: absolute;
    left: 0; right: 0;
    top: 134px;
    font-size: 32px;
    font-weight: 500;
    color: var(--accent-blue);
    line-height: 1;
  }
  .credentials {
    position: absolute;
    left: 0; right: 0;
    top: 175px;
    font-size: 32px;
    font-weight: 500;
    color: var(--text-grey);
    line-height: 1;
  }
  .contact-line {
    position: absolute;
    left: 0; right: 0;
    font-size: 32px;
    font-weight: 500;
    color: var(--text-grey);
    line-height: 1;
    letter-spacing: 0.3px;
  }
  .contact-email { top: 270px; }
  .contact-phone { top: 323px; }
  .contact-web { top: 370px; }
</style>
</head>
<body>
<div class="canvas">
  <div class="card-back"></div>
  <svg class="card-shadow" viewBox="0 0 943 26" preserveAspectRatio="none" aria-hidden="true">
    <defs>
      <linearGradient id="shadowFade" x1="0" y1="0" x2="1" y2="0">
        <stop offset="0" stop-color="var(--shadow-navy)" stop-opacity="0.9"/>
        <stop offset="0.5" stop-color="var(--shadow-navy)" stop-opacity="0.35"/>
        <stop offset="1" stop-color="var(--shadow-navy)" stop-opacity="0.9"/>
      </linearGradient>
      <filter id="shadowBlur"><feGaussianBlur stdDeviation="3"/></filter>
    </defs>
    <rect x="4" y="6" width="935" height="12" rx="6" fill="url(#shadowFade)" filter="url(#shadowBlur)"/>
  </svg>
  <div class="card-front">
    <h1 class="person-name">MARCUS DELLOW</h1>
    <p class="job-title">Director / Structural Engineer</p>
    <p class="credentials">BEng(Hons), CPEng, CMengNZ, IntPE(NZ)</p>
    <p class="contact-line contact-email">marcus.dellow@keystoneaudit.co.nz</p>
    <p class="contact-line contact-phone">0219364058</p>
    <p class="contact-line contact-web">www.keystoneaudit.co.nz</p>
  </div>
</div>
</body>
</html>
```